Mardi Gras 2013 Design Project

We have a design with elements that we want to retain. However, we need to take what we have and give it a creative BOOST!

Requirements
Must have
• Colors must stay, "KT" logo must stay,
Copy must remain (except - "Requests Your Presence" and small copy in bottom right corner);
Seal must remain, "9th Annual Velvet Lantern Gala" frame text can be modified but should resemble;
Gotham font to remain
Nice to have
• Any new Mardi Gras element - like a mask or beads - but can not over shadow copy

```html
<!DOCTYPE html>
<html lang="en">
<head>
<meta charset="utf-8">
<title>9th Annual Velvet Lantern Gala</title>
<link rel="stylesheet" href="https://fonts.googleapis.com/css2?family=Montserrat:ital,wght@0,500;0,700;0,800;0,900;1,700;1,800&display=swap">
<style>
  :root {
    --paper: #ffffff;
    --royal-purple: #4e3590;
    --deep-purple: #2d1a5c;
    --lilac: #8a63e0;
    --gold: #f2b53a;
    --green: #43b84b;
    --font-main: "Montserrat", Arial, sans-serif;
  }
  html, body {
    margin: 0;
    padding: 0;
    width: 1200px;
    height: 900px;
    overflow: hidden;
    background: var(--paper);
    font-family: var(--font-main);
  }
  .canvas {
    position: relative;
    width: 1200px;
    height: 900px;
  }
  .page {
    position: absolute;
    background: var(--royal-purple);
    overflow: hidden;
  }
  .page--front { left: 16px; top: 68px; width: 582px; height: 754px; }
  .page--back  { left: 638px; top: 70px; width: 546px; height: 756px; }

  .bead-strand {
    position: absolute;
    left: 14px;
    top: 4px;
    width: 100px;
    height: 460px;
    border-radius: 50px;
    background: linear-gradient(180deg, #4f9a52 0%, #d7b040 35%, #8e78c9 60%, #4f9a52 100%);
    opacity: 0.85;
  }
  .host {
    position: absolute;
    left: 82px;
    top: 62px;
    margin: 0;
    color: var(--gold);
    font-weight: 800;
    font-size: 17px;
    line-height: 21px;
    letter-spacing: 0.2px;
  }
  .seal {
    position: absolute;
    left: 404px;
    top: 20px;
    width: 160px;
    height: 160px;
    border-radius: 50%;
    background: var(--gold);
    display: flex;
    align-items: center;
    justify-content: center;
    text-align: center;
  }
  .seal__name {
    color: var(--deep-purple);
    font-weight: 800;
    font-size: 15px;
    line-height: 19px;
    text-transform: uppercase;
    width: 120px;
  }
  .title {
    position: absolute;
    left: 0;
    top: 0;
    width: 582px;
    height: 754px;
  }
  .title text {
    font-family: var(--font-main);
    font-style: italic;
    font-weight: 800;
    fill: none;
    stroke-width: 2;
  }
  .title .t-nine { stroke: var(--green); }
  .title .t-annual { stroke: var(--gold); }
  .title .t-velvet { stroke: var(--lilac); }
  .title .t-lantern { stroke: var(--green); }
  .title .t-gala { stroke: var(--gold); }
  .title .rule { stroke: var(--gold); stroke-width: 2; }

  .details {
    position: absolute;
    left: 186px;
    top: 506px;
    width: 392px;
    text-align: center;
    margin: 0;
  }
  .details p { margin: 0; }
  .details .day {
    color: var(--gold);
    font-weight: 500;
    font-size: 17px;
    letter-spacing: 2px;
    -webkit-text-stroke: 0.6px var(--deep-purple);
    line-height: 24px;
  }
  .details .date {
    color: var(--green);
    font-weight: 800;
    font-size: 22px;
    line-height: 32px;
  }
  .details .time,
  .details .at {
    color: var(--royal-purple);
    font-weight: 900;
    font-size: 17px;
    line-height: 24px;
    -webkit-text-stroke: 1px #b79cf0;
  }
  .details .venue-top {
    color: var(--gold);
    font-weight: 800;
    font-size: 18px;
    line-height: 30px;
    text-decoration: underline;
    text-underline-offset: 3px;
  }
  .details .venue {
    color: var(--gold);
    font-weight: 800;
    font-size: 22px;
    line-height: 30px;
  }
  .details .street {
    color: var(--green);
    font-weight: 700;
    font-size: 15px;
    line-height: 18px;
  }
  .details .city {
    color: var(--green);
    font-weight: 900;
    font-size: 31px;
    line-height: 40px;
    -webkit-text-stroke: 1.4px var(--deep-purple);
  }
  .mark-small {
    position: absolute;
    left: 20px;
    top: 622px;
    margin: 0;
    color: var(--gold);
    font-weight: 900;
    font-size: 92px;
    line-height: 1;
  }
  .mark-large {
    position: absolute;
    left: 0;
    top: 190px;
    width: 546px;
    margin: 0;
    text-align: center;
    color: var(--gold);
    font-weight: 900;
    font-size: 290px;
    line-height: 1;
  }
</style>
</head>
<body>
<main class="canvas">
  <section class="page page--front">
    <div class="bead-strand" role="img" aria-label="Twisted strand of green, gold and purple Mardi Gras beads"></div>
    <p class="host">THE ASSOCIATION OF<br>KINGSGATE TERRACE ALUMNI</p>
    <div class="seal"><span class="seal__name">Kingsgate Terrace High School</span></div>

    <svg class="title" viewBox="0 0 582 754" aria-label="9th Annual Velvet Lantern Gala">
      <text class="t-nine" x="332" y="247" font-size="160" text-anchor="middle" textLength="236" lengthAdjust="spacingAndGlyphs">9th</text>
      <text class="t-annual" x="309" y="287" font-size="44" text-anchor="middle" textLength="240" lengthAdjust="spacingAndGlyphs">ANNUAL</text>
      <text class="t-velvet" x="294" y="352" font-size="66" text-anchor="middle" textLength="290" lengthAdjust="spacingAndGlyphs">VELVET</text>
      <text class="t-lantern" x="297" y="417" font-size="60" text-anchor="middle" textLength="270" lengthAdjust="spacingAndGlyphs">LANTERN</text>
      <text class="t-gala" x="311" y="484" font-size="70" text-anchor="middle" textLength="232" lengthAdjust="spacingAndGlyphs">GALA</text>
      <line class="rule" x1="246" y1="498" x2="569" y2="498"/>
    </svg>

    <div class="details">
      <p class="day">SATURDAY</p>
      <p class="date">JANUARY 26,2013</p>
      <p class="time">7PM-12AM</p>
      <p class="at">AT THE</p>
      <p class="venue-top">PEACHTREE GRAND</p>
      <p class="venue">CONVENTION CENTER</p>
      <p class="street">1800 Meridian Hall Concourse</p>
      <p class="city">ATLANTA, GEORGIA</p>
    </div>

    <p class="mark-small">KT</p>
  </section>

  <section class="page page--back">
    <p class="mark-large">KT</p>
  </section>
</main>
</body>
</html>
```